Business Card needed for Drainor, a growing Septic Service company

Drainor, a growing local septic service company in Pennsylvania, needs updated business cards. We'd like the business card to feature our logo and communicate that we provide Septic Pumping, Installations/Repairs, Restroom Rentals, and 24/7 Emergency Service. The business card should be eye-catching, bold, and clean/simple. We have been in business almost 10 years and would like to expand and update our business brand and image.

Target Market(s)

Residential and Commercial, New and Current Homeowners

Industry/Entity Type

Service

Contact Information for Business Card

Contact on the business card should be: Dean Harlow Owner & Operator
Phone: 610-555-0187
Email: service@drainor-example.com
Website: www.drainor-example.com
Address: 812 Millbrook Lane Easton PA 18042

Font styles to use
Sans Serif

Colors

Designer to choose colors to be used in the design.

Requirements
Must have
• Feature logo on both side of business card.
Nice to have
• We envision the contact information on one side and our services listed on the other side. Utilize the green from the symbol in our logo as part of the design, overall design color scheme should be white, grey, black.

```html
<!DOCTYPE html>
<html lang="en">
<head>
<meta charset="utf-8">
<title>Drainor — Business Card</title>
<link rel="stylesheet" href="https://fonts.googleapis.com/css2?family=Noto+Sans:wght@400;700&family=Arimo:wght@400&display=swap">
<style>
  :root {
    --bg: #eceeed;
    --card: #ffffff;
    --ink: #252423;
    --green: #8dbf2e;
    --grey-text: #8a8a8a;
    --grey-rule: #a3a3a3;
  }
  * { margin: 0; padding: 0; box-sizing: border-box; }
  html, body {
    width: 1200px; height: 1091px; overflow: hidden;
    background: var(--bg);
    font-family: "Noto Sans", sans-serif;
  }
  .card {
    position: absolute;
    width: 704px; height: 406px;
    background: var(--card);
    border-radius: 16px;
    overflow: hidden;
  }
  .card--front { left: 123px; top: 109px; }
  .card--back { left: 357px; top: 567px; }

  .front-panel {
    position: absolute; left: 0; top: 0;
    width: 365px; height: 100%;
    background: var(--ink);
  }

  .brand {
    position: absolute;
    display: flex; align-items: center;
    font-family: "Noto Sans", sans-serif;
    font-weight: 700;
    color: var(--ink);
    letter-spacing: 0.5px;
  }
  .brand__mark { background: var(--green); flex: none; }
  .brand--front { right: 29px; top: 27px; font-size: 40px; gap: 10px; height: 43px; }
  .brand--front .brand__mark { width: 43px; height: 43px; }
  .brand--back { left: 48px; top: 176px; font-size: 50px; gap: 13px; height: 54px; }
  .brand--back .brand__mark { width: 54px; height: 54px; }

  .person { position: absolute; right: 29px; top: 94px; text-align: right; }
  .person__name { color: var(--green); font-weight: 700; font-size: 24px; line-height: 30px; }
  .person__role { color: var(--ink); font-size: 19px; line-height: 28px; }

  .contact { position: absolute; left: 339px; top: 259px; list-style: none; }
  .contact__item {
    display: flex; align-items: center;
    height: 30px;
    font-size: 17px; color: var(--ink); letter-spacing: 0.4px;
    white-space: nowrap;
  }
  .contact__icon { width: 18px; height: 18px; margin-right: 14px; flex: none; }

  .divider {
    position: absolute; left: 396px; top: 154px;
    width: 2px; height: 99px; background: var(--grey-rule);
  }
  .services {
    position: absolute; left: 440px; top: 153px; list-style: none;
    font-family: "Arimo", sans-serif; font-size: 19px; color: var(--grey-text);
  }
  .services__item { display: flex; align-items: center; height: 26.3px; }
  .services__item::before {
    content: ""; width: 6px; height: 6px; background: var(--green);
    margin-right: 6px; flex: none;
  }
</style>
</head>
<body>
  <section class="card card--front">
    <div class="front-panel"></div>
    <div class="brand brand--front"><span class="brand__mark"></span><span>DRAINOR</span></div>
    <div class="person">
      <p class="person__name">Dean Harlow</p>
      <p class="person__role">Owner &amp; Operator</p>
    </div>
    <ul class="contact">
      <li class="contact__item">
        <svg class="contact__icon" viewBox="0 0 20 20" aria-hidden="true"><path fill="#fff" d="M2 6c0-2 3-3 8-3s8 1 8 3v2h-4V6.5c-1-.5-2.5-.7-4-.7s-3 .2-4 .7V8H2zM5 9h10l2 8H3z"/></svg>
        610-555-0187
      </li>
      <li class="contact__item">
        <svg class="contact__icon" viewBox="0 0 20 20" aria-hidden="true"><rect x="3" y="5" width="14" height="11" fill="none" stroke="#fff" stroke-width="2"/><path d="M4 6l6 6 6-6" fill="none" stroke="#fff" stroke-width="2"/></svg>
        service@drainor-example.com
      </li>
      <li class="contact__item">
        <svg class="contact__icon" viewBox="0 0 20 20" aria-hidden="true"><g fill="none" stroke="#fff" stroke-width="1.4"><circle cx="10" cy="10" r="8"/><ellipse cx="10" cy="10" rx="3.5" ry="8"/><path d="M2 10h16M3.5 6h13M3.5 14h13"/></g></svg>
        www.drainor-example.com
      </li>
      <li class="contact__item">
        <svg class="contact__icon" viewBox="0 0 20 20" aria-hidden="true"><path fill="#fff" d="M10 1a6 6 0 0 0-6 6c0 5 6 12 6 12s6-7 6-12a6 6 0 0 0-6-6zm0 8.5A2.5 2.5 0 1 1 10 4.5a2.5 2.5 0 0 1 0 5z"/></svg>
        812 Millbrook Lane Elmton PA 18999
      </li>
    </ul>
  </section>

  <section class="card card--back">
    <div class="brand brand--back"><span class="brand__mark"></span><span>DRAINOR</span></div>
    <div class="divider"></div>
    <ul class="services">
      <li class="services__item">Septic Pumping</li>
      <li class="services__item">Installations/Repairs</li>
      <li class="services__item">Restroom Rentals</li>
      <li class="services__item">24/7 Emergency Service</li>
    </ul>
  </section>
</body>
</html>
```